Vantor Peak Solutions Landing Page

Vantor Peak Solutions provides Big Data Services to Small Businesses I am looking for a simple and elegant landing page. I am not advertising direct to end users. I am advertising to referral sources. My message is that I can show you how to make more money, grow your practice and become more valuable by offering these 8 services.

Target Market(s)

TallyNest CertPartners, CPA's, Accountants, Bookkeepers, and IT professionals

Industry/Entity Type

Accounting

Font styles to use
Sans Serif

Colors
3276b5
00a990

Requirements
Must have
• The standard components of a landing page Elegant, Professional and sophisticated design.

```html
<!DOCTYPE html>
<html lang="en">
<head>
<meta charset="utf-8">
<title>Vantor Peak Solutions</title>
<link href="https://fonts.googleapis.com/css2?family=Dosis:wght@400;500;600;700&family=Roboto+Condensed:wght@400;700&family=Lora:ital,wght@1,700&display=swap" rel="stylesheet">
<style>
:root{
  --brand:#3a6fc4;
  --brand-dark:#2b4b80;
  --ink:#444a55;
  --muted:#8a8f98;
  --night:#05070d;
  --footer:#0f1523;
  --footer-bar:#070a12;
  --grey-band:#f4f4f4;
  --white:#ffffff;
}
*{margin:0;padding:0;box-sizing:border-box}
html,body{width:1200px;height:2182px;overflow:hidden}
body{position:relative;background:var(--white);font-family:"Dosis",sans-serif;color:var(--ink)}
.abs{position:absolute}
.top-rule{left:0;top:0;width:1200px;height:4px;background:var(--brand)}
.bottom-rule{left:0;top:2177px;width:1200px;height:5px;background:var(--brand)}

/* hero */
.hero{left:0;top:4px;width:1200px;height:526px;background:var(--night);overflow:hidden}
.hero-photo{left:444px;top:0;width:756px;height:526px;
  background:linear-gradient(90deg,#05070d 0%,#1b1d22 28%,#6a6a6c 52%,#2a2c30 68%,#0a2a44 82%,#0f4a78 100%)}
.brand-name{font-family:"Dosis",sans-serif;font-weight:700;color:var(--brand);text-transform:uppercase;white-space:nowrap}
.hero-logo{left:157px;top:44px;font-size:22px;letter-spacing:1.5px}
.footer-logo{left:125px;top:1954px;font-size:17px;letter-spacing:1px}
.util-nav{top:20px;display:flex;gap:10px;align-items:center;color:var(--white);font-size:14px;font-weight:500}
.util-nav svg{width:16px;height:16px}
.main-nav{left:707px;top:70px;display:flex;align-items:center;color:var(--white);font-size:16px;font-weight:500}
.main-nav a{color:inherit;text-decoration:none;padding-bottom:6px}
.main-nav a.active{color:#6e9de6;border-bottom:2px solid #6e9de6}
.main-nav .sep{margin:0 16px;padding-bottom:6px}
.hero-title{left:121px;top:218px;font-size:24px;font-weight:700;color:var(--white)}
.hero-text{left:121px;top:260px;width:318px;font-size:14.5px;line-height:24px;color:var(--white)}
.btn{display:flex;align-items:center;justify-content:center;gap:8px;border-radius:21px;font-size:14px;font-weight:600;text-transform:uppercase}
.btn svg{width:8px;height:10px}
.hero-btn{left:124px;top:354px;width:131px;height:41px;border:1.5px solid var(--white);color:var(--white)}
.dots{left:575px;top:505px;display:flex;gap:8px}
.dots span{width:13px;height:13px;border-radius:50%;background:var(--white)}
.dots span.on{background:var(--brand)}

/* business */
.biz-title{left:127px;top:596px;font-size:22px;font-weight:600;color:#4a4f58}
.biz-text{left:127px;top:633px;width:510px;font-size:14px;line-height:22px;color:#6a6f78}
.biz-text p+p{margin-top:22px}
.biz-btn{left:127px;top:830px;width:131px;height:41px;border:1.5px solid var(--brand);color:var(--brand)}
.video{left:660px;top:602px;width:415px;height:228px;
  background:radial-gradient(ellipse at 50% 45%,#c98a2a 0%,#7a4a1e 35%,#3b3030 70%,#2a2a2e 100%)}
.play{left:838px;top:688px;width:58px;height:58px}

/* policy */
.policy{left:4px;top:919px;width:1196px;height:431px;background:var(--grey-band)}
.policy-title{left:0;top:960px;width:1200px;text-align:center;font-family:"Roboto Condensed",sans-serif;font-weight:700;font-size:19px;color:#4a4f58}
.policy-sub{left:0;top:995px;width:1200px;text-align:center;font-family:"Roboto Condensed",sans-serif;font-size:14px;color:#4a4f58}
.policy-sub b{color:var(--brand)}
.service{width:200px;text-align:center}
.service svg{width:48px;height:48px;display:block;margin:0 auto 8px}
.service h3{font-size:16px;font-weight:600;color:#4a4f58}
.service p{font-size:13px;color:var(--muted);margin-top:6px}
.service.feature h3,.service.feature p{color:var(--brand)}

/* testimonial */
.testimonial{left:0;top:1350px;width:1200px;height:317px;background:linear-gradient(115deg,#2d4f86 0%,#2b4a7e 60%,#2f5089 60%,#2f5089 100%)}
.t-title{left:0;top:1378px;width:1200px;text-align:center;color:var(--white);font-size:22px;font-weight:700}
.quote-box{left:271px;top:1465px;width:657px;height:97px;border:1px dashed rgba(255,255,255,.35);display:flex;align-items:center;padding:0 22px;
  font-family:"Lora",serif;font-style:italic;font-weight:700;font-size:13px;line-height:23px;color:var(--white)}
.quote-badge{left:567px;top:1442px;width:50px;height:42px}
.arrow-btn{width:22px;height:28px}
.avatar{left:509px;top:1571px;width:40px;height:40px;border-radius:50%;background:radial-gradient(circle,#d0d0d0,#8a8a8a);border:2px solid #fff}
.t-name{left:429px;top:1616px;width:200px;text-align:center;font-family:"Lora",serif;font-style:italic;font-weight:700;font-size:13px;color:var(--white)}

/* providers */
.prov-title{left:0;top:1712px;width:1200px;text-align:center;font-size:22px;font-weight:600;color:#4a4f58}
.providers{left:165px;top:1782px;width:880px;display:flex;justify-content:space-between;align-items:center}
.providers span{font-family:"Dosis",sans-serif;font-weight:700;font-size:22px;color:#3c4a5e}

/* footer */
.footer{left:0;top:1863px;width:1200px;height:261px;background:var(--footer)}
.f-label{font-size:13px;color:var(--white);text-transform:uppercase}
.f-col{top:1913px;color:var(--white);font-size:13px;text-transform:uppercase}
.f-col h4{font-weight:700;font-size:13px;margin-bottom:14px}
.f-col li{list-style:none;margin-bottom:13px}
.newsletter{left:877px;top:1913px}
.newsletter h4{color:var(--white);font-weight:700;font-size:13px;text-transform:uppercase}
.email{margin-top:22px;width:201px;height:35px;background:var(--white);display:flex;align-items:center;gap:8px;padding-left:10px;font-style:italic;font-size:12px;color:#777}
.email svg{width:16px;height:16px}
.signup{margin-top:12px;width:85px;height:35px;background:var(--brand);color:var(--white);font-weight:700;font-size:13px;display:flex;align-items:center;justify-content:center}
.foot-bar{left:0;top:2124px;width:1200px;height:53px;background:var(--footer-bar)}
.copy{left:129px;top:2140px;color:var(--white);font-style:italic;font-size:13px}
.social{left:952px;top:2140px;display:flex;gap:6px}
.social span{width:21px;height:21px;border-radius:50%}
</style>
</head>
<body>
<div class="abs top-rule"></div>

<header class="abs hero">
  <div class="abs hero-photo" role="img" aria-label="Profile portrait of a woman in greyscale beside glowing blue binary code"></div>
  <div class="abs brand-name hero-logo">Vantor Peak Solutions</div>
  <div class="abs util-nav" style="left:918px">
    <svg viewBox="0 0 16 16" fill="none" stroke="#fff" stroke-width="1.3"><path d="M7 2h7v12H7M1 8h9M7 5l3 3-3 3"/></svg>LOG IN
  </div>
  <div class="abs util-nav" style="left:1011px">
    <svg viewBox="0 0 16 16" fill="none" stroke="#fff" stroke-width="1.3"><circle cx="8" cy="5" r="3.3"/><path d="M2 15c0-3.5 2.7-5.5 6-5.5s6 2 6 5.5"/></svg>SIGN UP
  </div>
  <nav class="abs main-nav">
    <a class="active">HOME</a><span class="sep">I</span>
    <a>ABOUT</a><span class="sep">I</span>
    <a>HOW IT WORKS</a><span class="sep">I</span>
    <a>CONTRACT US</a>
  </nav>
  <h1 class="abs hero-title">Nisi ut aliquip ex ea comquat</h1>
  <p class="abs hero-text">Lorem ipsum dolor sit amet, consectetur adipisicing elit, sed do eiusmod tempor incididunt ut labore et dolore magna aliqua. Ut enim ad minim veniam...</p>
  <div class="abs btn hero-btn">Read More <svg viewBox="0 0 8 10"><path d="M1 1l5 4-5 4" fill="none" stroke="#fff" stroke-width="2"/></svg></div>
  <div class="abs dots"><span></span><span class="on"></span><span></span></div>
</header>

<section>
  <h2 class="abs biz-title">Know Our Business:</h2>
  <div class="abs biz-text">
    <p>Lorem ipsum dolor sit amet, consectetur adipisicing elit, sed do eiusmod tempor incididunt ut labore et dolore magna aliqua. Ut enim ad minim veniam, quis nostrud exercitation ullamco laboris nisi ut aliquip ex ea commodo consequat.</p>
    <p>Duis aute irure dolor in reprehenderit in voluptate velit esse cillum dolore eu fugiat nulla pariatur. Excepteur sint occaecat cupidatat non proident, sunt in culpa qui officia deserunt mollit anim id est laborum. Sed ut perspiciatis unde omnis iste natus error sit voluptatem accusantium</p>
  </div>
  <div class="abs btn biz-btn">Read More <svg viewBox="0 0 8 10"><path d="M1 1l5 4-5 4" fill="none" stroke="#3a6fc4" stroke-width="2"/></svg></div>
  <div class="abs video" role="img" aria-label="Video still of a hand-drawn idea light bulb on a desk with people working"></div>
  <svg class="abs play" viewBox="0 0 58 58" fill="none" stroke="#fff" stroke-width="2.5"><circle cx="29" cy="29" r="27"/><path d="M23 18l15 11-15 11z"/></svg>
</section>

<section>
  <div class="abs policy"></div>
  <h2 class="abs policy-title">KNOW DETAILS ABOUT OUR POLICY</h2>
  <p class="abs policy-sub">I can show you how to make more money, grow your practice and become more valuable by offering these <b>8 SERVICES.</b></p>

  <div class="abs service feature" style="left:168px;top:1058px">
    <svg viewBox="0 0 48 48" fill="none" stroke="#3a6fc4" stroke-width="1.6"><circle cx="24" cy="24" r="8"/><path d="M24 4l3 5 6-2 1 6 6 1-2 6 5 4-5 4 2 6-6 1-1 6-6-2-3 5-3-5-6 2-1-6-6-1 2-6-5-4 5-4-2-6 6-1 1-6 6 2z"/></svg>
    <h3>Lorem ipsum</h3><p>perspiciatis unde</p>
  </div>
  <div class="abs service" style="left:379px;top:1058px">
    <svg viewBox="0 0 48 48" fill="none" stroke="#555" stroke-width="1.6"><circle cx="18" cy="18" r="11"/><circle cx="30" cy="30" r="11" fill="#f4f4f4"/><path d="M30 24v11M26 31l4 4 4-4M15 16a3 3 0 1 1 6 0M14 22h8"/></svg>
    <h3>incididunt ut</h3><p>All in one Place</p>
  </div>
  <div class="abs service" style="left:604px;top:1058px">
    <svg viewBox="0 0 48 48" fill="none" stroke="#555" stroke-width="1.6"><path d="M10 8h20v30H10zM16 8v14l3-3 3 3V8M30 30h8M34 26v14M31 33l3-3 3 3"/></svg>
    <h3>quis nostrud</h3><p>voluptatem quia</p>
  </div>
  <div class="abs service" style="left:831px;top:1058px">
    <svg viewBox="0 0 48 48" fill="none" stroke="#555" stroke-width="1.6"><path d="M8 30l24 0 8-8-24 0zM8 26l24 0 8-8-24 0zM8 22l24 0 8-8-24 0zM14 26l22-4"/></svg>
    <h3>commodo consequat</h3><p>doloremque laudantium</p>
  </div>

  <div class="abs service feature" style="left:168px;top:1192px">
    <svg viewBox="0 0 48 48" fill="none"></svg>
    <h3>Lorem ipsum</h3><p>perspiciatis unde</p>
  </div>
  <div class="abs service" style="left:379px;top:1192px">
    <svg viewBox="0 0 48 48" fill="none" stroke="#555" stroke-width="1.6"><circle cx="18" cy="18" r="11"/><circle cx="30" cy="30" r="11" fill="#f4f4f4"/><path d="M30 24v11M26 31l4 4 4-4M15 16a3 3 0 1 1 6 0M14 22h8"/></svg>
    <h3>incididunt ut</h3><p>All in one Place</p>
  </div>
  <div class="abs service" style="left:604px;top:1192px">
    <svg viewBox="0 0 48 48" fill="none" stroke="#555" stroke-width="1.6"><path d="M10 8h20v30H10zM16 8v14l3-3 3 3V8M30 30h8M34 26v14M31 33l3-3 3 3"/></svg>
    <h3>quis nostrud</h3><p>voluptatem quia</p>
  </div>
  <div class="abs service" style="left:831px;top:1192px">
    <svg viewBox="0 0 48 48" fill="none" stroke="#555" stroke-width="1.6"><path d="M8 30l24 0 8-8-24 0zM8 26l24 0 8-8-24 0zM8 22l24 0 8-8-24 0zM14 26l22-4"/></svg>
    <h3>commodo consequat</h3><p>doloremque laudantium</p>
  </div>
</section>

<section>
  <div class="abs testimonial"></div>
  <h2 class="abs t-title">Enjoy Our Testimonial</h2>
  <div class="abs quote-box">"New home page is EXACTLY what was needed. This is better than any previous version...and certainly what I was looking for to keep my bills and finances organized. Thank you very much!"</div>
  <svg class="abs quote-badge" viewBox="0 0 50 42"><path d="M4 2h42a3 3 0 0 1 3 3v22a3 3 0 0 1-3 3H31l-6 10-6-10H4a3 3 0 0 1-3-3V5a3 3 0 0 1 3-3z" fill="#3a7fd6"/><text x="25" y="22" text-anchor="middle" font-family="Dosis,sans-serif" font-weight="700" font-size="17" fill="#fff">99</text></svg>
  <svg class="abs arrow-btn" style="left:124px;top:1494px" viewBox="0 0 22 28"><path d="M15 4L6 14l9 10" fill="none" stroke="#4a6aa0" stroke-width="3"/></svg>
  <svg class="abs arrow-btn" style="left:1057px;top:1494px" viewBox="0 0 22 28"><path d="M7 4l9 10-9 10" fill="none" stroke="#fff" stroke-width="3"/></svg>
  <div class="abs avatar" role="img" aria-label="Client portrait"></div>
  <div class="abs t-name">Mara Lindqvist</div>
</section>

<section>
  <h2 class="abs prov-title">Our Supported Popular Providers</h2>
  <svg class="abs arrow-btn" style="left:126px;top:1785px" viewBox="0 0 22 28"><path d="M14 6l-8 8 8 8" fill="none" stroke="#333" stroke-width="2.5"/></svg>
  <div class="abs providers">
    <span>Halcyra</span><span>Brightvolt</span><span>Linqo</span><span>Vistacast</span><span>Corvanet</span><span>Roadwise</span><span>Garnet Power</span>
  </div>
  <svg class="abs arrow-btn" style="left:1062px;top:1785px" viewBox="0 0 22 28"><path d="M8 6l8 8-8 8" fill="none" stroke="#6bb33a" stroke-width="2.5"/></svg>
</section>

<footer>
  <div class="abs footer"></div>
  <div class="abs f-label" style="left:128px;top:1913px">Powered by</div>
  <div class="abs brand-name footer-logo">Vantor Peak Solutions</div>
  <div class="abs f-col" style="left:409px">
    <h4>Esse cillum</h4>
    <ul><li>Dolore</li><li>Eu fugiat</li><li>Nulla</li><li>Pariatur.</li></ul>
  </div>
  <div class="abs f-col" style="left:639px">
    <h4>Sint</h4>
    <ul><li>Occaecat</li><li>Cupidatat non</li><li>Proident,</li><li>Sunt</li><li>In culpa</li></ul>
  </div>
  <div class="abs newsletter">
    <h4>Signup to our newsletter</h4>
    <div class="email"><svg viewBox="0 0 16 16" fill="none" stroke="#999" stroke-width="1.2"><circle cx="8" cy="8" r="7"/><rect x="4" y="5.5" width="8" height="5"/><path d="M4 5.5l4 3 4-3"/></svg>write email address here</div>
    <div class="signup">SIGNUP</div>
  </div>
  <div class="abs foot-bar"></div>
  <p class="abs copy">Copyright- VANTOR PEAK SOLUTIONS. All rights reserved 2016.</p>
  <div class="abs social">
    <span style="background:#3b5aa0"></span><span style="background:#e0452f"></span><span style="background:#1a86c4"></span><span style="background:#2aa9e8"></span><span style="background:#d9252a"></span>
  </div>
</footer>

<div class="abs bottom-rule"></div>
</body>
</html>
```